Smart Home App Needs 4 Mockup Screens. Extra Work Guaranteed for Winner

BACKGROUND
Our company, Lumora, is launching an exciting new app early next year. And we need some examples of what our app will look like to show to some of the biggest retailers in the world. We hope that this project will lead to regular work as we have a lot of new products planned for the app.

Our app will support baby, home and pet monitors (cameras) as well as the world's first smart pet flap.

The monitors allow you to do much more than just watch live video. By monitoring and providing information on sound, movement and temperature the app provides the user with instant peace of mind wherever they are. If anything has changed the user can be alerted via notifications. If motion is detected the user will receive a clip of the whole event moments after it has happened.

The Smart Pet Flap is packed full of features too. From letting you decide when your pet can or can't go outside from your mobile, to automatically opening if a fire is detected (along with a whole host of other features) - this really is the most advanced pet flap in the world.

REQUIREMENTS
We need 4 mock-up screens creating to show the UI of our app.
1. Camera Home Page
2. Camera Notifications Page
3. Pet Flap Fire Alarm Warning Page
4. Extreme Weather Warning Page

Optional - Happy to Pay the Winner Extra for these Designs
5. Start Up/Log In Page
6. Pet Flap Notification Example
7. Pet Flap Scheduler Page (your choice)
(SEE LUMORA APP DESIGN COMPETITION - ATTACHED)

STYLE GUIDE
As you'll see from our wireframes we want our app to be very minimal and modern. The predominant colour will be white but where colour is used it should be bright (see our colour palette - which we will provide shortly).

INSPIRATION
We love the UI of Finchly (home surveillance). Also check out Vesk (smart thermostat).
(SEE LUMORA UI EXAMPLES ATTACHED)

LOGO
We love our logo. Feel free to use it in creative ways.

So far we're also using it as a kind of beacon to indicate if everything is ok.

LOGO COLOURS & APP COLOURS
As mentioned, we are thinking of using the green logo to indicate that everything is ok (and also for the pet app in general). We reserve red for when something has happened (normally bad) and needs attention, like a fire alarm going off.

The app will be predominantly black and white with the odd minimal flash of colour (probably primary colour)
We'll upload a colour scheme as soon as we have it.

CONTACT
Please message us for more details - we'll do our best to reply promptly.

FUTURE WORK
We will need extra screens made straight after the competition is over and there should be additional regular work after this.

Target Market(s)

Our app will be used by young professionals, to young parents to grandparents. The design must be contemporary but timeless and easy to use no matter how good you are with technology.

Industry/Entity Type

Pet

Font styles to use
Sans Serif

Colors
faee3f
33a6d7
ec1f27
acd036
32b7a4

Requirements
Must have
• Beautiful, minimal design. Make sure you spend time looking at the Finchly and Vesk apps before starting.

For the videos make sure you use sensible images - that you'd expect to see from a monitor (high resolution images if possible)
Nice to have
• Creative use of our logo.
Should not have
• Too much detail/clutter/colours. Ugly fonts.

```html
<!DOCTYPE html>
<html lang="en">
<head>
<meta charset="utf-8">
<title>Lumora – Camera Home</title>
<link rel="stylesheet" href="https://fonts.googleapis.com/css2?family=Open+Sans:wght@300;400;600&display=swap">
<style>
  :root {
    --page-bg: #f4f4f4;
    --screen-bg: #ffffff;
    --ink: #111111;
    --ink-soft: #333333;
    --label: #3a3a3a;
    --chevron: #9a9a9a;
    --tab-active: #ebebeb;
    --control-band: #9c9c9c;
    --control-btn: #ffffff;
    --icon: #8a8a8a;
  }
  * { box-sizing: border-box; margin: 0; padding: 0; }
  html, body {
    width: 900px; height: 1200px; overflow: hidden;
    background: var(--page-bg);
    font-family: "Open Sans", Helvetica, Arial, sans-serif;
  }
  .screen {
    position: absolute; left: 120px; top: 16px;
    width: 659px; height: 1168px;
    background: var(--screen-bg);
    overflow: hidden;
  }
  /* status bar */
  .status-bar {
    position: absolute; left: 0; top: 0; width: 100%; height: 45px;
    display: flex; align-items: center; justify-content: space-between;
    padding: 0 14px; font-size: 22px; color: var(--ink);
  }
  .status-left, .status-right { display: flex; align-items: center; gap: 8px; }
  .status-time { position: absolute; left: 0; right: 0; text-align: center; font-weight: 600; pointer-events: none; }
  /* nav bar */
  .nav-bar { position: absolute; left: 0; top: 45px; width: 100%; height: 78px; }
  .menu-icon { position: absolute; left: 28px; top: 22px; }
  .tab {
    position: absolute; top: 0; height: 78px;
    display: flex; align-items: center; justify-content: center;
    font-size: 19px; color: var(--ink-soft); letter-spacing: 0.5px;
  }
  .tab-now { left: 408px; width: 123px; background: var(--tab-active); }
  .tab-earlier { left: 531px; width: 128px; }
  .tab-pointer { position: absolute; left: 457px; top: 123px; z-index: 2; }
  /* live view */
  .live-view {
    position: absolute; left: 0; top: 123px; width: 100%; height: 370px;
    background: linear-gradient(135deg, #d9c9bd 0%, #c9b3a6 40%, #8b7a72 70%, #b69f95 100%);
  }
  /* controls */
  .controls {
    position: absolute; left: 0; top: 493px; width: 100%; height: 125px;
    background: var(--control-band);
  }
  .control-btn {
    position: absolute; top: 21px; width: 83px; height: 83px; border-radius: 50%;
    background: var(--control-btn);
    display: flex; align-items: center; justify-content: center;
  }
  /* camera list */
  .camera-list { position: absolute; left: 0; top: 648px; width: 100%; list-style: none; }
  .camera-row { position: relative; height: 165px; }
  .camera-thumb { position: absolute; left: 30px; top: 0; width: 246px; height: 139px; }
  .thumb-kitchen { background: linear-gradient(180deg, #c79a63 0%, #8a6a4c 55%, #c9a37a 100%); }
  .thumb-patio { background: linear-gradient(180deg, #6f6e63 0%, #8b5a49 55%, #6e705d 100%); }
  .thumb-pets { background: linear-gradient(180deg, #d8d8dc 0%, #8c8683 55%, #3e3330 100%); }
  .camera-name {
    position: absolute; left: 357px; top: 56px;
    font-size: 20px; font-weight: 400; color: var(--label);
  }
  .camera-chevron { position: absolute; left: 616px; top: 59px; }
</style>
</head>
<body>
<main class="screen">
  <header class="status-bar">
    <div class="status-left">
      <svg width="78" height="14" viewBox="0 0 78 14" aria-hidden="true">
        <circle cx="7" cy="7" r="6" fill="#111"/><circle cx="23" cy="7" r="6" fill="#111"/><circle cx="39" cy="7" r="6" fill="#111"/>
        <circle cx="55" cy="7" r="5.3" fill="none" stroke="#111" stroke-width="1.4"/><circle cx="71" cy="7" r="5.3" fill="none" stroke="#111" stroke-width="1.4"/>
      </svg>
      <span>VOLT</span>
      <svg width="26" height="20" viewBox="0 0 26 20" aria-hidden="true">
        <path d="M2 7 A16 16 0 0 1 24 7" fill="none" stroke="#111" stroke-width="2.6"/>
        <path d="M6.5 11 A10 10 0 0 1 19.5 11" fill="none" stroke="#111" stroke-width="2.6"/>
        <path d="M13 19 L9.5 14.5 A5 5 0 0 1 16.5 14.5 Z" fill="#111"/>
      </svg>
    </div>
    <span class="status-time">4:21 PM</span>
    <div class="status-right">
      <svg width="14" height="22" viewBox="0 0 14 22" aria-hidden="true">
        <path d="M2 6 L12 15 L7 20 V2 L12 7 L2 16" fill="none" stroke="#111" stroke-width="1.6"/>
      </svg>
      <span>100%</span>
      <svg width="48" height="22" viewBox="0 0 48 22" aria-hidden="true">
        <rect x="1" y="2" width="42" height="18" rx="3" fill="none" stroke="#111" stroke-width="1.6"/>
        <rect x="4" y="5" width="36" height="12" rx="1.5" fill="#111"/>
        <rect x="44.5" y="8" width="3" height="6" rx="1" fill="#111"/>
      </svg>
    </div>
  </header>

  <nav class="nav-bar">
    <svg class="menu-icon" width="52" height="34" viewBox="0 0 52 34" aria-label="Menu" role="img">
      <rect y="0" width="52" height="5" fill="#111"/><rect y="14" width="52" height="5" fill="#111"/><rect y="28" width="52" height="5" fill="#111"/>
    </svg>
    <div class="tab tab-now">NOW</div>
    <div class="tab tab-earlier">EARLIER</div>
  </nav>
  <svg class="tab-pointer" width="26" height="14" viewBox="0 0 26 14" aria-hidden="true">
    <path d="M0 0 H26 L13 14 Z" fill="var(--tab-active)"/>
  </svg>

  <section class="live-view" role="img" aria-label="Live camera view of a baby sleeping in a crib beside a soft toy"></section>

  <section class="controls">
    <div class="control-btn" style="left:81px" aria-label="Talk">
      <svg width="40" height="48" viewBox="0 0 40 48" aria-hidden="true">
        <rect x="13" y="3" width="14" height="26" rx="7" fill="none" stroke="var(--icon)" stroke-width="2.4"/>
        <path d="M7 22 A13 13 0 0 0 33 22" fill="none" stroke="var(--icon)" stroke-width="2.4"/>
        <line x1="20" y1="35" x2="20" y2="44" stroke="var(--icon)" stroke-width="2.4"/>
      </svg>
    </div>
    <div class="control-btn" style="left:215px" aria-label="Temperature">
      <svg width="30" height="54" viewBox="0 0 30 54" aria-hidden="true">
        <path d="M10 8 A5 5 0 0 1 20 8 V34 A10 10 0 1 1 10 34 Z" fill="none" stroke="var(--icon)" stroke-width="2.4"/>
        <rect x="13" y="22" width="4" height="18" fill="var(--icon)"/>
        <circle cx="15" cy="42" r="6" fill="var(--icon)"/>
      </svg>
    </div>
    <div class="control-btn" style="left:359px" aria-label="Activity">
      <svg width="42" height="42" viewBox="0 0 42 42" aria-hidden="true">
        <rect x="2" y="22" width="10" height="18" fill="var(--icon)"/>
        <rect x="16" y="12" width="10" height="28" fill="var(--icon)"/>
        <rect x="30" y="2" width="10" height="38" fill="var(--icon)"/>
      </svg>
    </div>
    <div class="control-btn" style="left:493px" aria-label="Move camera">
      <svg width="62" height="62" viewBox="0 0 62 62" aria-hidden="true">
        <g fill="none" stroke="var(--icon)" stroke-width="2" stroke-linejoin="round">
          <line x1="31" y1="4" x2="31" y2="58"/><line x1="4" y1="31" x2="58" y2="31"/>
          <path d="M23 12 L31 4 L39 12"/><path d="M23 50 L31 58 L39 50"/>
          <path d="M12 23 L4 31 L12 39"/><path d="M50 23 L58 31 L50 39"/>
        </g>
      </svg>
    </div>
  </section>

  <ul class="camera-list">
    <li class="camera-row">
      <div class="camera-thumb thumb-kitchen" role="img" aria-label="Kitchen camera view of wooden cabinets and an island"></div>
      <span class="camera-name">Kitchen Camera</span>
      <svg class="camera-chevron" width="10" height="20" viewBox="0 0 10 20" aria-hidden="true"><path d="M2 1 L8 10 L2 19" fill="none" stroke="var(--chevron)" stroke-width="1.4"/></svg>
    </li>
    <li class="camera-row">
      <div class="camera-thumb thumb-patio" role="img" aria-label="Patio camera view of a brick courtyard with potted plants"></div>
      <span class="camera-name">Patio Camera</span>
      <svg class="camera-chevron" width="10" height="20" viewBox="0 0 10 20" aria-hidden="true"><path d="M2 1 L8 10 L2 19" fill="none" stroke="var(--chevron)" stroke-width="1.4"/></svg>
    </li>
    <li class="camera-row">
      <div class="camera-thumb thumb-pets" role="img" aria-label="Pets camera view of a cat and a dog resting on a rug"></div>
      <span class="camera-name">Pets Camera</span>
      <svg class="camera-chevron" width="10" height="20" viewBox="0 0 10 20" aria-hidden="true"><path d="M2 1 L8 10 L2 19" fill="none" stroke="var(--chevron)" stroke-width="1.4"/></svg>
    </li>
  </ul>
</main>
</body>
</html>
```